Bright Harbor Capital website

Build a website template for the Bright Harbor Capital fund.
Looking for a cool website design showing companies we are using the latest in web design trends. We want to attract app developers, typically the younger set.
A good example of one of our competitive firms is http://mossfinch.org
The required components for the website include:
1) Funding application
2) about our firm
a) Partner profiles - We will include photographs and bios about each of the partners in our firm.
b) Invest with Bright Harbor - This will include information how to invest with our fund
c) our process - About our process for evaluating, funding and helping build successful businesses - This will include a narrative about the target companies, how we work, the type of deals we are interested in, our expectations, etc ...
3) Investment profiles - Stories about the companies we invest with
4) News - Output from our twitter feed and copies of our Blog posts

```html
<!DOCTYPE html>
<html lang="en">
<head>
<meta charset="utf-8">
<title>Bright Harbor Capital</title>
<link rel="stylesheet" href="https://fonts.googleapis.com/css2?family=Roboto+Condensed:wght@400;700&family=Arimo:wght@400;700&family=EB+Garamond&display=swap">
<style>
:root{
  --green:#6cc04a;
  --green-dark:#4e9e31;
  --topbar:#3b3b3b;
  --ink:#2f2f2f;
  --text:#555;
  --muted:#777;
  --band:#c9c9c9;
  --band-line:#e6e6e6;
  --panel:#c2c2c2;
  --navy:#1f3c80;
  --orange:#f0a12b;
  --white:#fff;
}
*{margin:0;padding:0;box-sizing:border-box}
html,body{width:860px;height:1200px;overflow:hidden}
body{position:relative;background:var(--white);font-family:"Roboto Condensed",Arial,sans-serif;color:var(--text)}
.abs{position:absolute}

/* top bar */
.topbar{left:0;top:0;width:860px;height:32px;background:var(--topbar);color:#ddd;font-size:10px}
.contact{left:107px;top:9px;display:flex;gap:22px;align-items:center}
.contact span{display:flex;align-items:center;gap:6px}
.social-top{right:107px;top:7px;display:flex;gap:8px}
.social-top i{display:block;width:16px;height:16px;border-radius:3px;background:#d8d8d8}

/* header */
.header{left:0;top:32px;width:860px;height:75px;background:var(--white);border-bottom:1px solid #e4e4e4}
.brand{left:107px;top:22px;display:flex;align-items:center;gap:8px}
.brand-dot{width:30px;height:30px;border-radius:50%;background:var(--green)}
.brand-name{font-family:"Arimo",Arial,sans-serif;font-weight:700;font-size:21px;color:var(--green);letter-spacing:-.3px}
.nav{left:390px;top:0;height:75px;display:flex;font-size:10px;color:#444}
.nav a{display:flex;align-items:center;padding:0 11px;height:75px;text-decoration:none;color:inherit;text-transform:uppercase}
.nav a.active{background:#f0f0f0;border-top:4px solid var(--green)}

/* hero */
.hero{left:0;top:107px;width:860px;height:217px;background:radial-gradient(ellipse at 72% 45%,#cfe3f7 0%,#6e9dd4 25%,#2d5ea8 55%,#173b78 100%)}
.hero-title{left:127px;top:42px;width:420px;font-family:"Arimo",Arial,sans-serif;font-weight:700;font-size:16px;line-height:22px;color:var(--white);text-transform:uppercase}
.hero-text{left:127px;top:90px;width:340px;font-size:11px;line-height:13px;color:#eef4ff;text-transform:uppercase}
.btn{display:inline-flex;align-items:center;justify-content:center;background:var(--green);color:var(--white);font-weight:700;text-decoration:none;border:1px solid #8fd872}
.hero-btn{left:127px;top:137px;width:140px;height:31px;font-size:12px;text-transform:uppercase}
.hero-arrow{top:98px;width:20px;height:20px;border:1.5px solid #e8f0ff;border-radius:50%}
.hero-arrow svg{display:block}

/* invest */
.section-title{font-family:"Arimo",Arial,sans-serif;font-weight:700;font-size:14px;color:var(--ink);text-transform:uppercase}
.invest-title{left:107px;top:380px}
.invest-text{left:107px;top:409px;width:388px;font-size:10px;line-height:13.6px;color:#555}
.quote{left:537px;top:348px;width:218px;height:220px;border-radius:4px;background:linear-gradient(#333,#4a4a4a 50%,#353535);border:1px solid #222}
.quote-title{left:0;top:14px;width:100%;text-align:center;font-size:15px;font-weight:700;color:var(--white);text-transform:uppercase}
.field{left:32px;width:150px;height:20px;background:#9a9a9a;border:1px solid #bbb;font-size:9px;color:#e8e8e8;padding:3px 6px}
.field.area{height:46px}
.select-caret{right:6px;top:7px}
.submit{left:120px;top:180px;width:62px;height:22px;background:linear-gradient(#555,#222);border:1px solid #999;color:var(--white);font-size:12px;display:flex;align-items:center;justify-content:center}

/* how we work */
.work{left:0;top:591px;width:860px;height:253px;background:var(--band)}
.work-title{left:107px;top:16px}
.steps{left:107px;top:45px;width:650px;height:172px}
.step-num{width:24px;height:24px;border-radius:50%;background:var(--green);border:2px solid #fff;color:#fff;font-weight:700;font-size:14px;display:flex;align-items:center;justify-content:center}
.step-name{top:20px;font-family:"Arimo",Arial,sans-serif;font-size:22px;line-height:26px;color:var(--white);letter-spacing:-.3px}
.step-text{top:51px;width:132px;font-size:10px;line-height:13.8px;color:#3f3f3f}
.step-btn{top:139px;width:69px;height:21px;font-size:11px;font-weight:400;border-radius:2px}

/* partners */
.partners-title{left:107px;top:861px}
.pager{left:413px;top:858px;display:flex;gap:8px}
.divider{left:479px;top:862px;width:1px;height:237px;background:#ddd}
.partner{width:170px;height:70px}
.photo{left:0;top:0;width:68px;height:68px;background:linear-gradient(#3a5f8e,#223c5e)}
.p-name{left:76px;top:0;font-size:11px;color:var(--ink)}
.p-role{left:76px;top:15px;width:80px;font-size:11px;line-height:13px;color:var(--muted)}
.p-btn{left:76px;top:50px;width:68px;height:17px;font-size:10px;font-weight:400;justify-content:space-between;padding:0 8px}

/* news */
.news-title{left:527px;top:861px}
.news-item{left:527px;width:228px}
.news-badge{left:0;top:0;width:42px;height:62px;border:1px solid #ccc}
.news-badge .thumb{left:0;top:0;width:40px;height:34px;background:#eee;display:flex;align-items:center;justify-content:center}
.news-badge .thumb i{display:block;width:22px;height:22px;border-radius:50%;background:#8a8a8a}
.news-badge .date{left:0;top:34px;width:40px;height:26px;background:var(--orange);color:#fff;text-align:center;font-size:11px;line-height:12px;padding-top:1px}
.news-head{left:48px;top:0;width:180px;font-size:11px;line-height:13px;color:var(--green);font-weight:400}
.news-body{left:48px;top:32px;width:180px;font-size:9.5px;line-height:13px;color:var(--muted)}
.news-rule{left:0;top:86px;width:228px;border-top:1px dashed #bbb}
.news-more{left:687px;top:1087px;width:68px;height:17px;font-size:10px;font-weight:400;justify-content:space-between;padding:0 8px}

/* footer */
.footer{left:0;top:1120px;width:860px;height:80px;background:var(--navy)}
.footer-social{left:371px;top:19px;display:flex;gap:5px}
.footer-social i{display:block;width:19px;height:19px;border-radius:3px}
.copyright{left:0;top:50px;width:860px;text-align:center;font-family:"EB Garamond",Georgia,serif;font-size:10px;color:#e3e8f5}
</style>
</head>
<body>

<div class="abs topbar">
  <div class="abs contact">
    <span><svg width="10" height="10" viewBox="0 0 10 10"><path d="M2 0.5l2 2-1 1.3c.6 1.3 1.6 2.3 2.9 2.9L7.2 5.7l2 2L8 9.5C4 9.3.7 6 .5 2z" fill="#ddd"/></svg>Phone : +22 555 010 284</span>
    <span><svg width="11" height="8" viewBox="0 0 11 8"><rect width="11" height="8" fill="#ddd"/><path d="M0 0l5.5 4.5L11 0" stroke="#3b3b3b" fill="none"/></svg>Mail : info@brightharbor.com</span>
  </div>
  <div class="abs social-top" aria-label="Social links"><i></i><i></i><i></i><i></i></div>
</div>

<header class="abs header">
  <div class="abs brand"><span class="brand-dot"></span><span class="brand-name">Bright Harbor Capital</span></div>
  <nav class="abs nav">
    <a class="active" href="#">Home</a>
    <a href="#">About us</a>
    <a href="#">Our partners</a>
    <a href="#">Investment profiles</a>
    <a href="#">News</a>
  </nav>
</header>

<section class="abs hero" role="img" aria-label="Businessman holding a glowing globe surrounded by app icons and currency symbols">
  <h1 class="abs hero-title">Invention portfolio for business agency and business individuals</h1>
  <p class="abs hero-text">Lorem Ipsum is simply dummy text of the printing and typesetting industry. Lorem Ipsum has been the industry's standard dummy text ever since the 1500s</p>
  <a class="abs btn hero-btn" href="#">Investment profiles</a>
  <span class="abs hero-arrow" style="left:81px"><svg width="17" height="17" viewBox="0 0 17 17"><path d="M10 4.5L6 8.5l4 4" stroke="#fff" stroke-width="1.6" fill="none"/></svg></span>
  <span class="abs hero-arrow" style="left:759px"><svg width="17" height="17" viewBox="0 0 17 17"><path d="M7 4.5l4 4-4 4" stroke="#fff" stroke-width="1.6" fill="none"/></svg></span>
</section>

<h2 class="abs section-title invest-title">Invest with Bright Harbor</h2>
<p class="abs invest-text">Lorem Ipsum is simply dummy text of the printing and typesetting industry. Lorem Ipsum has been the industry's standard dummy text ever since the 1500s, when an unknown printer took a galley of type and scrambled it to make a type specimen book. It has survived not only five centuries, but also the leap into electronic typesetting, remaining essentially unchanged. Lorem Ipsum is simply dummy text of the printing and typesetting industry. Lorem Ipsum has been the industry's standard dummy text ever since the 1500s, when an unknown printer took a galley of type and scrambled it to make a type specimen book. It has survived not only five centuries, but also the leap into electronic typesetting, remaining essentially unchanged.</p>

<form class="abs quote">
  <div class="abs quote-title">Request a quote</div>
  <div class="abs field" style="top:42px">Name</div>
  <div class="abs field" style="top:70px">Email</div>
  <div class="abs field" style="top:99px">Choose your portfolio<svg class="abs select-caret" width="7" height="5" viewBox="0 0 7 5"><path d="M0 0h7L3.5 5z" fill="#333"/></svg></div>
  <div class="abs field area" style="top:128px">Description</div>
  <div class="abs submit">Submit</div>
</form>

<section class="abs work">
  <h2 class="abs section-title work-title">How we work?</h2>
  <div class="abs steps">
    <svg class="abs" style="left:0;top:0" width="650" height="172" viewBox="0 0 650 172">
      <g fill="var(--panel)" stroke="var(--band-line)" stroke-width="1.5" stroke-linejoin="round">
        <path d="M4 1h163l53 85-53 85H4a3 3 0 0 1-3-3V4a3 3 0 0 1 3-3z"/>
        <path d="M167 1h206l53 85-53 85H167l53-85z"/>
        <path d="M373 1h220l53 85-53 85H373l53-85z"/>
      </g>
    </svg>

    <span class="abs step-num" style="left:9px;top:8px">1</span>
    <div class="abs step-name" style="left:44px">Evaluating</div>
    <p class="abs step-text" style="left:44px">Lorem Ipsum is simply dummy text of the printing and typeset-ting industry. Lorem Ipsum has been the industry's standard Lorem Ipsum is simply dummy text of the printing ting industry.</p>
    <a class="abs btn step-btn" style="left:44px" href="#">Read More</a>

    <span class="abs step-num" style="left:215px;top:8px">2</span>
    <div class="abs step-name" style="left:248px">Funding</div>
    <p class="abs step-text" style="left:248px">Lorem Ipsum is simply dummy text of the printing and typeset-ting industry. Lorem Ipsum has been the industry's standard Lorem Ipsum is simply dummy text of the printing ting industry.</p>
    <a class="abs btn step-btn" style="left:248px" href="#">Read More</a>

    <span class="abs step-num" style="left:420px;top:8px">3</span>
    <div class="abs step-name" style="left:453px">Growing</div>
    <p class="abs step-text" style="left:453px">Lorem Ipsum is simply dummy text of the printing and typeset-ting industry. Lorem Ipsum has been the industry's standard Lorem Ipsum is simply dummy text of the printing ting industry.</p>
    <a class="abs btn step-btn" style="left:453px" href="#">Read More</a>
  </div>
</section>

<h2 class="abs section-title partners-title">Partner profiles</h2>
<div class="abs pager"><svg width="7" height="10" viewBox="0 0 7 10"><path d="M5.5 1L1.5 5l4 4" stroke="#333" stroke-width="1.5" fill="none"/></svg><svg width="7" height="10" viewBox="0 0 7 10"><path d="M1.5 1l4 4-4 4" stroke="#333" stroke-width="1.5" fill="none"/></svg></div>
<div class="abs divider"></div>

<div class="abs partner" style="left:107px;top:893px">
  <div class="abs photo" role="img" aria-label="Portrait photo of partner"></div>
  <div class="abs p-name">Daniel Hartley</div>
  <div class="abs p-role">Event Moderator Principal.</div>
  <a class="abs btn p-btn" href="#">More <span>&raquo;</span></a>
</div>
<div class="abs partner" style="left:285px;top:893px">
  <div class="abs photo" role="img" aria-label="Portrait photo of partner"></div>
  <div class="abs p-name">Daniel Hartley</div>
  <div class="abs p-role">Event Moderator Principal.</div>
  <a class="abs btn p-btn" href="#">More <span>&raquo;</span></a>
</div>
<div class="abs partner" style="left:107px;top:992px">
  <div class="abs photo" role="img" aria-label="Portrait photo of partner"></div>
  <div class="abs p-name">Daniel Hartley</div>
  <div class="abs p-role">Event Moderator Principal.</div>
  <a class="abs btn p-btn" href="#">More <span>&raquo;</span></a>
</div>
<div class="abs partner" style="left:285px;top:992px">
  <div class="abs photo" role="img" aria-label="Portrait photo of partner"></div>
  <div class="abs p-name">Daniel Hartley</div>
  <div class="abs p-role">Event Moderator Principal.</div>
  <a class="abs btn p-btn" href="#">More <span>&raquo;</span></a>
</div>

<h2 class="abs section-title news-title">Latest news</h2>
<article class="abs news-item" style="top:893px;height:90px">
  <div class="abs news-badge"><div class="abs thumb"><i></i></div><div class="abs date">DEC<br>27</div></div>
  <h3 class="abs news-head">Microdata and Structura.org for all your Searchly rich snippet needs</h3>
  <p class="abs news-body">I recently shared my insights about Searchly rich snippets, Structura.org, and microdata at Search Summit Pro on the panel session.</p>
  <div class="abs news-rule"></div>
</article>
<article class="abs news-item" style="top:992px;height:90px">
  <div class="abs news-badge"><div class="abs thumb"><i></i></div><div class="abs date">DEC<br>27</div></div>
  <h3 class="abs news-head">Microdata and Structura.org for all your Searchly rich snippet needs</h3>
  <p class="abs news-body">I recently shared my insights about Searchly rich snippets, Structura.org, and microdata at Search Summit Pro on the panel session.</p>
  <div class="abs news-rule"></div>
</article>
<a class="abs btn news-more" href="#">More <span>&raquo;</span></a>

<footer class="abs footer">
  <div class="abs footer-social" aria-label="Social links">
    <i style="background:#2fa9e0"></i><i style="background:#3b5a9a"></i><i style="background:#dd4b39"></i><i style="background:#1ab7ea"></i><i style="background:#e52d27"></i>
  </div>
  <p class="abs copyright">© 2014 Bright Harbor Capital. All Rights Reserved.</p>
</footer>

</body>
</html>
```